Business Card for a Little Gothic Online Shoe Business
Velvet Moth Treasures
Business Card for a Little Gothic Online Shoe Business - Apparel
Creative Brief
Bright & Fun-filled
9 Carrowby Street Kelvin Flats QLD 4826
velvetmothtreasures@mailbrook.net
www.velvetmothtreasures-shop.com.au
ABN: 41 285 607 952
In addition to Business card designs I would also like to see designs for Letterhead and Envelope.
This should be a really funky fresh design to match the Business Logo. Our Colours are Purple and Black but Im open to others as long as the Business Logo is not changed. I also like the idea of incorpating Candy Striping or Old Victorian Floral Motifs in the Card I do not want any Shoes on the card as we also do Clothes etc

```html
<!DOCTYPE html>
<html lang="en">
<head>
<meta charset="utf-8">
<title>Velvet Moth Treasures – Business Card</title>
<link href="https://fonts.googleapis.com/css2?family=Fredoka:wght@600&family=Open+Sans:wght@400;600&display=swap" rel="stylesheet">
<style>
  :root {
    --purple: #5e2a96;
    --purple-mid: #7a45b3;
    --purple-light: #9d74c9;
    --lavender: #d8c8ea;
    --card-white: #f4f3f6;
    --ink: #4a2a6e;
    --backdrop: #d9d9dc;
  }
  * { margin: 0; padding: 0; box-sizing: border-box; }
  html, body { width: 1200px; height: 874px; overflow: hidden; }
  body {
    background: var(--backdrop);
    font-family: "Open Sans", sans-serif;
    position: relative;
  }
  .card {
    position: absolute;
    top: 272px;
    width: 540px;
    height: 330px;
    border-radius: 16px;
    overflow: hidden;
    box-shadow: 0 6px 18px rgba(0,0,0,0.18);
  }
  .card--front {
    left: 40px;
    background:
      repeating-linear-gradient(90deg, var(--purple) 0 14px, var(--purple-mid) 14px 24px);
  }
  .card--back {
    left: 620px;
    background: var(--card-white);
  }
  .brand {
    position: absolute;
    display: flex;
    flex-direction: column;
    align-items: center;
    gap: 14px;
  }
  .brand__dot {
    width: 86px; height: 86px;
    border-radius: 50%;
  }
  .brand__name {
    font-family: "Fredoka", sans-serif;
    font-weight: 600;
    font-size: 34px;
    line-height: 1.05;
    text-align: center;
  }
  .card--front .brand { left: 0; right: 0; top: 78px; }
  .card--front .brand__dot { background: var(--card-white); }
  .card--front .brand__name { color: var(--card-white); }
  .card--back .brand { left: 34px; top: 78px; width: 230px; }
  .card--back .brand__dot { background: var(--purple); }
  .card--back .brand__name { color: var(--purple); font-size: 30px; }
  .wave { position: absolute; inset: 0; }
  .contact {
    position: absolute;
    right: 26px;
    top: 22px;
    text-align: right;
    font-size: 11px;
    line-height: 1.5;
    color: var(--ink);
  }
  .contact__group { margin-bottom: 6px; }
  .abn {
    position: absolute;
    left: 34px;
    bottom: 22px;
    font-size: 10px;
    color: var(--ink);
    letter-spacing: 0.3px;
  }
</style>
</head>
<body>
  <section class="card card--front" aria-label="Card front">
    <div class="brand">
      <span class="brand__dot"></span>
      <span class="brand__name">Velvet Moth<br>Treasures</span>
    </div>
  </section>

  <section class="card card--back" aria-label="Card back">
    <svg class="wave" viewBox="0 0 540 330" preserveAspectRatio="none" aria-hidden="true">
      <path d="M540 150 C480 190 440 230 410 265 C380 300 320 320 220 330 L540 330 Z" fill="var(--lavender)"/>
      <path d="M540 170 C490 205 455 245 430 275 C405 305 355 322 280 330 L540 330 Z" fill="var(--purple-light)"/>
      <path d="M540 190 C500 220 470 255 450 285 C430 312 395 326 340 330 L540 330 Z" fill="var(--purple)"/>
      <path d="M300 330 C360 318 400 300 425 272" fill="none" stroke="var(--card-white)" stroke-width="2"/>
    </svg>
    <div class="brand">
      <span class="brand__dot"></span>
      <span class="brand__name">Velvet Moth<br>Treasures</span>
    </div>
    <div class="contact">
      <div class="contact__group">
        <div>9 Carrowby Street</div>
        <div>Kelvin Flats QLD 4826</div>
      </div>
      <div class="contact__group">
        <div>0400 318 552</div>
      </div>
      <div class="contact__group">
        <div>velvetmothtreasures@mailbrook.net</div>
        <div>www.velvetmothtreasures-shop.com.au</div>
      </div>
    </div>
    <div class="abn">ABN: 41 285 607 952</div>
  </section>
</body>
</html>
```